Maple Ledger Business Card

Colors can be blue, grey and white as you see in the attached logo. Needs to have a spot for name, title, phone, email, address, and website. There also needs to be a spot for an agent's picture.

Contact Information for Business Card

See project description.

Colors

Designer to choose colors to be used in the design.

```html
<!DOCTYPE html>
<html lang="en">
<head>
<meta charset="utf-8">
<title>Maple Ledger Business Card</title>
<link href="https://fonts.googleapis.com/css2?family=Montserrat:wght@400;500;600;700&display=swap" rel="stylesheet">
<style>
  :root {
    --brand-blue: #3478b6;
    --brand-blue-light: #3f86c2;
    --charcoal: #3c3c3e;
    --text-grey: #444446;
    --paper: #ffffff;
    --portrait-tone: #e6edf4;
    --portrait-edge: #c9d7e6;
    --backdrop: #2a2a2c;
  }
  * { box-sizing: border-box; margin: 0; padding: 0; }
  html, body {
    width: 1200px; height: 900px; overflow: hidden;
    background: var(--backdrop);
    font-family: "Montserrat", Arial, sans-serif;
  }
  .sheet {
    width: 1200px; height: 900px;
    display: flex; flex-direction: column; align-items: center; justify-content: center;
    gap: 60px;
  }
  .card {
    position: relative;
    width: 630px; height: 360px;
    overflow: hidden;
  }
  .card-front {
    background: linear-gradient(135deg, var(--brand-blue) 0%, var(--brand-blue-light) 100%);
    display: flex; align-items: center; justify-content: center;
  }
  .brand-lockup {
    display: flex; align-items: center; gap: 10px;
    color: var(--paper);
    font-weight: 700;
    letter-spacing: 2px;
    text-transform: uppercase;
    white-space: nowrap;
  }
  .brand-lockup .brand-square {
    width: 18px; height: 18px; background: var(--paper); flex: none;
  }
  .card-front .brand-lockup { font-size: 30px; }
  .card-back { background: var(--paper); }
  .card-back .wave { position: absolute; inset: 0; }
  .card-back .brand-lockup {
    position: absolute; right: 30px; top: 66px;
    font-size: 22px;
  }
  .card-back .brand-lockup .brand-square { width: 13px; height: 13px; }
  .person {
    position: absolute; left: 34px; top: 92px;
    color: var(--text-grey);
  }
  .person-name {
    font-size: 21px; font-weight: 600; letter-spacing: 1.5px; text-transform: uppercase;
  }
  .person-title { font-size: 14px; font-weight: 400; margin-top: 2px; }
  .agent-photo {
    position: absolute; left: 34px; top: 148px;
    width: 86px; height: 86px; border-radius: 50%;
    background: linear-gradient(160deg, var(--portrait-tone) 0%, var(--portrait-edge) 100%);
    border: 3px solid var(--brand-blue);
  }
  .contact {
    position: absolute; left: 34px; bottom: 30px;
    color: var(--text-grey);
    font-size: 15px; line-height: 1.55; letter-spacing: 0.6px;
    list-style: none;
  }
  .contact .accent { color: var(--brand-blue); }
  .address {
    position: absolute; right: 34px; bottom: 30px;
    color: var(--text-grey);
    font-size: 15px; line-height: 1.55; letter-spacing: 0.6px;
    text-align: right; font-style: normal;
  }
</style>
</head>
<body>
<main class="sheet">
  <section class="card card-front">
    <div class="brand-lockup"><span class="brand-square"></span><span>Maple Ledger</span></div>
  </section>

  <section class="card card-back">
    <svg class="wave" width="630" height="360" viewBox="0 0 630 360" aria-hidden="true">
      <path fill="var(--brand-blue)" d="M0 62 C150 50 250 70 322 130 C250 90 150 74 0 82 Z"/>
      <path fill="var(--charcoal)" d="M0 0 H630 V230 C520 226 420 193 330 138 C250 78 150 48 0 57 Z"/>
      <path fill="var(--paper)" d="M0 0 H630 V217 C520 213 420 180 330 125 C250 65 150 35 0 45 Z"/>
      <path fill="var(--brand-blue)" d="M0 0 H630 V212 C520 208 420 175 330 120 C250 60 150 30 0 40 Z"/>
    </svg>
    <div class="brand-lockup"><span class="brand-square"></span><span>Maple Ledger</span></div>
    <div class="person">
      <p class="person-name">Daniel Whitaker</p>
      <p class="person-title">Director</p>
    </div>
    <div class="agent-photo" role="img" aria-label="Agent portrait photo"></div>
    <ul class="contact">
      <li>(555) 014-2387</li>
      <li>info@mapleledger.com</li>
      <li>www.<span class="accent">mapleledger</span>.com</li>
    </ul>
    <address class="address">712 Cedar Hollow<br>Drive Reno, NV 89501</address>
  </section>
</main>
</body>
</html>
```